Newspaper Ad Design Project

We are launching a new business support telephone helpline, using the following copy:

"Calling all Midlands manufacturers - Discover how to make it better!

Call The Fabrication Knowledge Desk
08000 73 91 25
Signposting – Sourcing – Connecting

One of the region’s leading business support agencies - Forged Across Wessex has launched a free phone telephone line The Fabrication Knowledge Desk.

This new service is is open to manufacturers seeking advice, help and intelligence on any aspect of their business:

1) Funding Sources
2) Referrals and Business Opportunities
3) Innovation and New Product Development
4) Apprenticeships, Education and Training
5) Working with Supply Chains
6) Events and Networking Opportunities
7) Marketing and Promotional Activity
8) Other help

If you need help with a manufacturing query our dedicated team of professionals can help you today. No automated lines, just one-to-one advice helping you to find the right solution to improve your bottom line.

The Fabrication Knowledge Desk – 08000 73 91 25

www.forgedacrosswessex.com
@forgedwessex"

Target Market(s)

SME Manufacturers in the Midlands area of England

Industry/Entity Type

Business

Requirements
Must have
• It must include all of the copy outlined in the brief, our logo, website and social media addresses.

Size wise it must be 100mm deep by 305mm wide.

If selected your design will potentially be used in other media.

```html
<!DOCTYPE html>
<html lang="en">
<head>
<meta charset="utf-8">
<title>Fabrication Knowledge Desk – Newspaper Ad</title>
<link rel="stylesheet" href="https://fonts.googleapis.com/css2?family=Open+Sans:wght@400;600;700;800&display=swap">
<style>
  :root {
    --page-bg: #ecebe8;
    --red: #c8202b;
    --green: #3e9d63;
    --blue: #23a0cf;
    --yellow: #efaa1f;
    --orange: #e4741a;
    --white: #ffffff;
    --ink-red: #c8202b;
  }
  * { margin: 0; padding: 0; box-sizing: border-box; }
  html, body {
    width: 1200px; height: 1029px; overflow: hidden;
    background: var(--page-bg);
    font-family: "Open Sans", Arial, sans-serif;
    color: var(--white);
  }
  .ad {
    position: absolute; left: 40px; top: 331px;
    width: 1120px; height: 366px;
  }
  .ad > section { position: absolute; }

  /* Header band */
  .header { left: 0; top: 0; width: 1120px; height: 146px; background: var(--red); }
  .header__headline {
    position: absolute; left: 22px; top: 12px;
    font-size: 27px; font-weight: 700; letter-spacing: 0.2px; white-space: nowrap;
  }
  .header__service {
    position: absolute; left: 22px; top: 58px;
    font-size: 21px; font-weight: 700; white-space: nowrap;
  }
  .header__intro {
    position: absolute; left: 22px; top: 92px; width: 700px;
    font-size: 13.5px; line-height: 1.35; font-weight: 400;
  }
  .phone-pill {
    position: absolute; left: 731px; top: 54px; width: 360px; height: 58px;
    background: var(--white); border-radius: 29px;
    display: flex; align-items: center; padding-left: 8px;
  }
  .phone-pill svg { width: 46px; height: 46px; flex: none; }
  .phone-pill__number {
    margin-left: 14px; color: var(--ink-red);
    font-size: 31px; font-weight: 700; white-space: nowrap;
  }
  .header__tagline {
    position: absolute; left: 750px; top: 117px;
    font-size: 18px; font-weight: 600; white-space: nowrap;
  }

  /* Services list */
  .services { left: 0; top: 146px; width: 829px; height: 139px; background: var(--green); }
  .services__intro {
    position: absolute; left: 22px; top: 8px; width: 600px;
    font-size: 14px; font-weight: 700; line-height: 1.3;
  }
  .services__list {
    position: absolute; left: 22px; top: 46px; width: 800px;
    list-style: none;
    display: grid; grid-template-columns: 420px 380px; row-gap: 1px;
    font-size: 15.5px; font-weight: 700; line-height: 1.3;
  }
  .services__list li { white-space: nowrap; }

  /* Contact strip */
  .contact { left: 0; top: 285px; width: 829px; height: 81px; background: var(--yellow); }
  .contact__text {
    position: absolute; left: 22px; top: 4px; width: 790px;
    font-size: 13.5px; line-height: 1.4; font-weight: 400;
  }
  .contact__bar {
    position: absolute; left: 0; top: 46px; width: 485px; height: 35px;
    background: var(--orange);
    padding-left: 22px; display: flex; align-items: center;
    font-size: 14px; font-weight: 700; white-space: nowrap;
  }

  /* Brand panel */
  .brand { left: 829px; top: 146px; width: 291px; height: 220px; background: var(--blue); }
  .brand__mark {
    position: absolute; left: 96px; top: 12px; width: 98px; height: 98px;
    border-radius: 50%; background: var(--white);
  }
  .brand__name {
    position: absolute; left: 0; top: 112px; width: 291px; text-align: center;
    font-size: 15px; font-weight: 700;
  }
  .brand__web {
    position: absolute; left: 0; top: 138px; width: 291px; text-align: center;
    font-size: 13px; font-weight: 400;
  }
  .brand__social {
    position: absolute; left: 0; top: 172px; width: 291px; text-align: center;
    font-size: 20px; font-weight: 700;
  }
</style>
</head>
<body>
<main class="ad" aria-label="Fabrication Knowledge Desk helpline advertisement">

  <section class="header">
    <h1 class="header__headline">Calling all Midlands manufacturers - Discover how to make it better</h1>
    <h2 class="header__service">Call The Fabrication Knowledge Desk</h2>
    <p class="header__intro">One of the region’s leading business support agencies - Forged Across Wessex has launched a free phone telephone line The Fabrication Knowledge Desk.</p>
    <div class="phone-pill">
      <svg viewBox="0 0 46 46" aria-hidden="true">
        <circle cx="23" cy="23" r="23" fill="#c8202b"/>
        <path d="M16 12c1-1 2.5-1 3.3.2l2.4 3.6c.6 1 .4 2.2-.4 3l-1.6 1.5c1.2 2.8 3.2 4.9 6 6.2l1.6-1.6c.8-.8 2-1 3-.4l3.6 2.3c1.2.8 1.3 2.3.3 3.3l-1.8 1.8c-1.4 1.4-3.6 1.8-5.4.9-6.2-3-10.7-7.6-13.6-13.8-.8-1.8-.4-3.9 1-5.3z" fill="#fff"/>
      </svg>
      <span class="phone-pill__number">08000 73 91 25</span>
    </div>
    <p class="header__tagline">Signposting – Sourcing – Connecting</p>
  </section>

  <section class="services">
    <p class="services__intro">This new service is is open to manufacturers seeking advice, help and intelligence on any aspect of their business:</p>
    <ol class="services__list">
      <li>1) Funding Sources</li>
      <li>2) Referrals and Business Opportunities</li>
      <li>3) Innovation and New Product Development</li>
      <li>4) Apprenticeships, Education and Training</li>
      <li>5) Working with Supply Chains</li>
      <li>6) Events and Networking Opportunities</li>
      <li>7) Marketing and Promotional Activity</li>
      <li>8) Other help</li>
    </ol>
  </section>

  <section class="contact">
    <p class="contact__text">If you need help with a manufacturing query our dedicated team of professionals can help you today. No automated lines, just one-to-one advice helping you to find the right solution to improve your bottom line.</p>
    <p class="contact__bar">The Fabrication Knowledge Desk – 08000 73 91 25</p>
  </section>

  <section class="brand">
    <div class="brand__mark" aria-hidden="true"></div>
    <p class="brand__name">Forged Across Wessex</p>
    <p class="brand__web">www.forgedacrosswessex.com</p>
    <p class="brand__social">@forgedwessex</p>
  </section>

</main>
</body>
</html>
```